We are looking for a simple design that would be uplifting for
upscale drug addicts

MERIDIAN COLLECTIVE

PLEASE SEE THE LINK FOR TAG LINE AND CONTENT

thank you.

here is all the actual info we need and we want something like this...

http://files.qzr.lumtrabox.example/rest/objects/7c2910e4b557d81a93e40bd59fa644163fe2adf0899f?uid=bdf8e1b9b6f556b6b83c44471fdc79%2fproofs&expires=1482716603&signature=kT9PwLmQxZbVoNHLdtrtlmoGHQB%3d

The shape and colors don't have to be like what I posted it is only an example.

Target Market(s)

Harlow Row, internet and creative types, men, early 30's,
upwardly mobile, drug addicts

current site

brightkestrelway.example

now launching new name Meridian Collective

Industry/Entity Type

Drug

Requirements
Must have
• upscale look, great font
Should not have
• a corporate look but should not look like a clinic.

```html
<!DOCTYPE html>
<html lang="en">
<head>
<meta charset="utf-8">
<title>Meridian Collective – Business Card</title>
<link rel="stylesheet" href="https://fonts.googleapis.com/css2?family=Michroma&family=Open+Sans:wght@400;600;700&display=swap">
<style>
  :root {
    --brand-blue: #05628a;
    --brand-blue-dark: #044f70;
    --card-white: #ffffff;
    --tab-grey: #c9ccce;
    --backdrop: #b9b9b9;
    --ink-light: #eaf3f7;
  }
  * { box-sizing: border-box; margin: 0; padding: 0; }
  html, body { width: 1200px; height: 896px; overflow: hidden; }
  body {
    background: var(--backdrop);
    font-family: "Open Sans", Arial, sans-serif;
    position: relative;
  }
  .card {
    position: absolute;
    top: 294px;
    width: 525px;
    height: 300px;
    overflow: hidden;
    box-shadow: 0 6px 18px rgba(0,0,0,0.25);
  }

  /* Front */
  .card--front { left: 50px; background: var(--card-white); }
  .front__accent-bar {
    position: absolute; left: 0; top: 0; width: 100%; height: 6px;
    background: var(--brand-blue);
  }
  .front__block {
    position: absolute; left: 0; top: 98px; width: 40px; height: 56px;
    background: var(--brand-blue);
  }
  .front__company {
    position: absolute; left: 58px; top: 30px;
    font-family: "Michroma", "Arial Black", sans-serif;
    font-variant: small-caps;
    color: var(--brand-blue);
    font-size: 30px; line-height: 32px; letter-spacing: 2px;
  }
  .front__company span { display: block; }
  .front__company .line-1 { padding-left: 70px; }
  .front__person { position: absolute; left: 52px; top: 104px; color: var(--brand-blue); }
  .front__name { font-weight: 700; font-size: 22px; letter-spacing: 0.5px; line-height: 24px; }
  .front__role { font-size: 12px; letter-spacing: 5px; margin-top: 1px; }
  .front__contact {
    position: absolute; left: 300px; top: 186px;
    list-style: none; color: var(--brand-blue);
    font-weight: 600; font-size: 11px; line-height: 14px;
  }
  .front__contact li { display: flex; align-items: flex-start; gap: 10px; margin-bottom: 5px; }
  .front__contact svg { width: 14px; height: 14px; flex: none; fill: var(--brand-blue); }

  /* Back */
  .card--back { left: 625px; background: var(--brand-blue); }
  .back__company {
    position: absolute; right: 40px; top: 112px;
    font-family: "Michroma", "Arial Black", sans-serif;
    font-variant: small-caps;
    color: var(--card-white);
    font-size: 22px; letter-spacing: 2px;
  }
  .back__tab {
    position: absolute; right: 0; top: 150px; width: 12px; height: 28px;
    background: var(--tab-grey);
  }
  .back__social {
    position: absolute; left: 28px; bottom: 40px; right: 28px;
    display: flex; justify-content: space-between; list-style: none;
    color: var(--ink-light); font-size: 11px;
  }
  .back__social li { display: flex; align-items: center; gap: 7px; }
  .social-mark { width: 16px; height: 16px; background: var(--card-white); }
  .social-mark--round { border-radius: 50%; }
</style>
</head>
<body>

<section class="card card--front" aria-label="Business card front">
  <div class="front__accent-bar"></div>
  <div class="front__block"></div>
  <h1 class="front__company"><span class="line-1">Meridian</span><span>Collective</span></h1>
  <div class="front__person">
    <p class="front__name">MARCUS HALE</p>
    <p class="front__role">GENERAL MANAGER</p>
  </div>
  <ul class="front__contact">
    <li>
      <svg viewBox="0 0 16 16" aria-hidden="true"><path d="M8 1 1 7.5h2V15h4v-4h2v4h4V7.5h2z"/></svg>
      <span>041.12th floor.Arc<br>Lindell Road KVR</span>
    </li>
    <li>
      <svg viewBox="0 0 16 16" aria-hidden="true"><circle cx="8" cy="8" r="6.5" fill="none" stroke="#05628a" stroke-width="1.4"/><path d="M1.5 8h13M8 1.5v13" stroke="#05628a" stroke-width="1.2" fill="none"/><ellipse cx="8" cy="8" rx="3" ry="6.5" fill="none" stroke="#05628a" stroke-width="1.2"/></svg>
      <span>www.meridiancollective.example</span>
    </li>
    <li>
      <svg viewBox="0 0 16 16" aria-hidden="true"><rect x="1" y="3.5" width="14" height="9"/><path d="M1 3.5 8 9l7-5.5" stroke="#fff" stroke-width="1.2" fill="none"/></svg>
      <span>hello@meridiancollective.example</span>
    </li>
    <li>
      <svg viewBox="0 0 16 16" aria-hidden="true"><path d="M4 1.5 6.3 4 5 6c.8 2 2.6 3.9 5 5l2-1.3 2.5 2.3-1.6 2.5C7.5 14 2 8.5 1.5 3z"/></svg>
      <span>014 382 5907</span>
    </li>
  </ul>
</section>

<section class="card card--back" aria-label="Business card back">
  <h2 class="back__company">Meridian Collective</h2>
  <div class="back__tab"></div>
  <ul class="back__social">
    <li><span class="social-mark"></span><span>meridianco</span></li>
    <li><span class="social-mark social-mark--round"></span><span>@meridianco</span></li>
    <li><span class="social-mark"></span><span>meridianco</span></li>
  </ul>
</section>

</body>
</html>
```